Landing Page Design Needed For Lead Generation capture.

We are a lead / appointment service specifically for the custom closet systems industry. We need a landing page created for a Wix site.
We need the winner to code the site for a Wix platform.
Winner will earn ongoing business.

The domain name format will be this format: www.WardrobeSage{City}.example
For example this first landing page is www.WardrobeSageGreenville.example
When we add new cities we will create new landing pages.

Wardrobe Sage Greenville will be the name of this first landing page so a simple logo is needed.

View this website first: www.ShelvingForge.example for inspiration and to learn about custom closet systems.

You can also use this site for copy inspiration and photo examples. Also the form is similar to what we need. (Must also be mobile optimized)

A slider showing showing the following would be helpful:

Our value and service.

Wardrobe Sage Greenville pre screens custom closet companies and matches home owners with the best company in their area / zip code. This saves home owners both time and money. Let Wardrobe Sage make it easy for you!

On the page, tell the visitor to use promo code SAGE500 to save $500 off any size closet system.

Here are names and descriptions for the slider photos:

1. Bedroom Closet - Closets as unique as you
2. Entertainment Center - Artfully entertaining
3. Laundry room - Make doing laundry FUN!
4. Home office - Make working from home smarter
5. Garage - Park in your garage again and find everything the first time!

The form should have the following fields.

"Schedule your free consultation with our pre screened closet designers"
- First and Last Name
- Email
- Phone
- Zip
(A check box for the following allowing multiple selections)
"I'm Interested In"
1. Bedroom Closet
2. Entertainment Center
3. Laundry room
4. Home office
5. Garage system

"Enter Promo Code"

Text at the bottom of the form:
"We use your zip code to align you with the nearest and best closet designers. We use your email and phone number to contact you and schedule your free design consultation."

The data from the submitted form will go to: leeds@WardrobeSageGreenville.example

Home owners

```html
<!DOCTYPE html>
<html lang="en">
<head>
<meta charset="utf-8">
<title>Wardrobe Sage Greenville</title>
<link href="https://fonts.googleapis.com/css2?family=Poppins:ital,wght@0,400;0,500;0,600;0,700;1,500&display=swap" rel="stylesheet">
<style>
:root{
  --navy:#1f1c4d;
  --navy-deep:#17153c;
  --yellow:#f6c43c;
  --lilac:#7f7da2;
  --white:#ffffff;
  --ink:#1b1a2e;
  --muted:#6f6d86;
  --field:#eeeef3;
}
*{margin:0;padding:0;box-sizing:border-box}
html,body{width:1200px;height:2848px;overflow:hidden}
body{font-family:"Poppins",sans-serif;color:var(--ink);background:var(--white);position:relative}
.abs{position:absolute}

/* hero */
.hero{left:0;top:0;width:1200px;height:560px;background:linear-gradient(180deg,#2a2760 0%,#3b3878 45%,#25224f 100%)}
.hero-photo{left:0;top:0;width:1200px;height:560px;background:radial-gradient(ellipse at 50% 40%,rgba(120,110,170,.45),rgba(20,18,50,.2) 70%)}
.topbar{left:20px;top:10px;font-size:11px;color:#d9d8ea;display:flex;gap:26px}
.logo{left:32px;top:48px;display:flex;align-items:center;gap:12px;color:var(--white);font-weight:600;font-size:20px;line-height:1.1}
.logo-mark{width:34px;height:34px;border:3px solid var(--white)}
.nav{left:720px;top:48px;height:80px;display:flex;align-items:center;gap:44px;font-size:14px;color:var(--white);font-weight:500}
.nav-contact{left:1032px;top:48px;width:168px;height:80px;background:var(--yellow);display:flex;align-items:center;justify-content:center;font-size:14px;font-weight:500;color:var(--ink)}
.hero-title{left:0;top:350px;width:1200px;text-align:center;color:var(--white);font-size:46px;font-weight:500;line-height:1.25}
.hero-title em{font-style:italic}
.search{left:272px;top:512px;width:656px;height:56px;background:var(--white);display:flex;align-items:center}
.search-loc{flex:1;display:flex;align-items:center;gap:12px;padding-left:22px;font-size:13px;color:var(--muted)}
.search-btn{width:128px;height:56px;background:var(--navy-deep);color:var(--white);font-size:13px;display:flex;align-items:center;justify-content:center}

/* about */
.about{left:0;top:560px;width:1200px;height:880px;background:var(--yellow)}
.eyebrow{font-size:12px;font-weight:600;letter-spacing:2px;color:var(--navy);text-transform:uppercase}
.about-eyebrow{left:0;top:102px;width:1200px;text-align:center}
.about-title{left:0;top:124px;width:1200px;text-align:center;font-size:40px;font-weight:700;line-height:1.2;color:var(--ink)}
.about-text{left:380px;top:222px;width:440px;text-align:center;font-size:13px;line-height:1.7;color:#7a6a3a}
.feature{top:328px;width:296px;height:456px;background:var(--lilac);color:var(--white);padding:0 28px 28px;display:flex;flex-direction:column;justify-content:flex-end}
.feature-photo{background:linear-gradient(180deg,#d9d4cf 0%,#8d7f78 50%,#3c3740 100%)}
.feature h3{font-size:24px;font-weight:600;margin-bottom:10px}
.feature p{font-size:13px;line-height:1.6;color:#ecebf5}

/* appointment */
.appoint-band{left:0;top:1440px;width:1200px;height:288px;background:var(--navy)}
.appoint{left:220px;top:1470px;width:880px;height:228px;background:var(--white);border-radius:24px;padding:16px 32px}
.appoint-head{display:flex;align-items:baseline;gap:14px;margin-bottom:8px}
.appoint-head h2{font-size:17px;font-weight:600}
.appoint-head p{font-size:11px;color:var(--muted)}
.appoint-row{display:flex;align-items:flex-end;gap:16px}
.field{width:192px}
.field label,.interest-label{display:block;font-size:12px;font-weight:600;margin-bottom:5px}
.field span{display:block;height:38px;border-radius:19px;background:var(--field);font-size:12px;color:#9a99ad;line-height:38px;text-align:center}
.row-two{margin-top:10px}
.interests{flex:1}
.checks{display:flex;gap:12px;font-size:11px;color:var(--ink);height:38px;align-items:center}
.check{display:flex;align-items:center;gap:5px;white-space:nowrap}
.check i{width:13px;height:13px;border:1.5px solid var(--navy);border-radius:3px;display:inline-block}
.promo{width:150px}
.book-btn{width:130px;height:40px;border-radius:20px;background:var(--navy-deep);color:var(--white);font-size:14px;font-weight:600;display:flex;align-items:center;justify-content:center}
.appoint-note{margin-top:10px;font-size:10px;line-height:1.45;color:var(--muted)}

/* projects */
.projects{left:0;top:1728px;width:1200px;height:532px;background:var(--yellow)}
.projects-eyebrow{left:220px;top:70px;font-size:12px;color:var(--ink);font-weight:500}
.projects-title{left:220px;top:92px;font-size:31px;font-weight:500;line-height:1.35;color:var(--ink)}
.arrows{left:900px;top:104px;display:flex;gap:16px}
.arrow{width:40px;height:40px;display:flex;align-items:center;justify-content:center}
.arrow-prev{background:#e2b236}
.arrow-next{background:var(--navy)}
.card{top:184px;width:216px;height:288px;background:var(--white)}
.card-img{height:176px}
.card-body{padding:22px 16px}
.card h4{font-size:15px;font-weight:600;line-height:1.2;white-space:nowrap}
.card p{font-size:11px;color:var(--muted);margin-top:4px}

/* offer */
.offer-tall{left:200px;top:2340px;width:200px;height:320px;background:linear-gradient(180deg,#f0f0f2,#c7c6cc 60%,#e9e8ec)}
.offer-small{width:100px;height:150px}
.offer-line{left:752px;top:2408px;width:80px;height:4px;background:var(--navy)}
.offer-eyebrow{left:752px;top:2424px;font-size:12px;color:var(--ink)}
.offer-title{left:752px;top:2452px;font-size:40px;font-weight:600;color:var(--navy);line-height:1.1}
.offer-text{left:752px;top:2520px;font-size:12px;color:var(--muted)}
.offer-btn{left:752px;top:2556px;height:44px;padding:0 22px;background:var(--navy-deep);color:var(--white);font-size:12px;display:flex;align-items:center;gap:10px}

.steps{left:200px;top:2716px;width:860px;display:flex;justify-content:space-between}
.step{display:flex;gap:12px;width:190px}
.step-num{font-size:28px;font-weight:700;color:var(--navy);line-height:1}
.step h5{font-size:13px;font-weight:600}
.step p{font-size:11px;color:var(--muted);line-height:1.4}
</style>
</head>
<body>

<section class="abs hero">
  <div class="abs hero-photo" role="img" aria-label="Dark walk-in closet with hanging clothes behind the hero"></div>
  <div class="abs topbar"><span>Email: leeds@WardrobeSageGreenville.example</span><span>Call: +1 555 010 2400</span></div>
  <div class="abs logo"><span class="logo-mark"></span><span>Wardrobe Sage<br>Greenville</span></div>
  <nav class="abs nav"><span>About Us</span><span>Gallery</span><span>Our Experts</span></nav>
  <div class="abs nav-contact">Contact</div>
  <h1 class="abs hero-title">A <em>different</em> approach to<br>afford yourself a dream home</h1>
  <div class="abs search">
    <div class="search-loc">
      <svg width="14" height="18" viewBox="0 0 14 18"><path d="M7 0C3.1 0 0 3.1 0 7c0 5 7 11 7 11s7-6 7-11C14 3.1 10.9 0 7 0zm0 9.5A2.5 2.5 0 1 1 7 4.5a2.5 2.5 0 0 1 0 5z" fill="#1f1c4d"/></svg>
      <span>Location</span>
    </div>
    <div class="search-btn">Search</div>
  </div>
</section>

<section class="abs about">
  <p class="abs eyebrow about-eyebrow">About Us</p>
  <h2 class="abs about-title">Powering a Sustainable<br>Future Together</h2>
  <p class="abs about-text">We pre-screen local closet companies and match you with the best designer near your zip code.</p>
  <article class="abs feature feature-photo" style="left:132px" role="img" aria-label="Closet rail with folded and hanging clothes">
    <h3>Renewable</h3>
  </article>
  <article class="abs feature" style="left:452px">
    <h3>Energy</h3>
    <p>Matched designers save you time and money on every custom closet project.</p>
  </article>
  <article class="abs feature" style="left:772px">
    <h3>Future</h3>
    <p>Use promo code SAGE500 to save $500 off any size closet system.</p>
  </article>
</section>

<section class="abs appoint-band"></section>
<form class="abs appoint">
  <div class="appoint-head">
    <h2>Make Appointment</h2>
    <p>Schedule your free consultation with our pre screened closet designers</p>
  </div>
  <div class="appoint-row">
    <div class="field"><label>First and Last Name</label><span>ex. John Smith</span></div>
    <div class="field"><label>Email</label><span>ex. name@mail.example</span></div>
    <div class="field"><label>Phone</label><span>ex. 555 0102</span></div>
    <div class="field"><label>Zip</label><span>ex. 29601</span></div>
  </div>
  <div class="appoint-row row-two">
    <div class="interests">
      <span class="interest-label">I'm Interested In</span>
      <div class="checks">
        <span class="check"><i></i>Bedroom Closet</span>
        <span class="check"><i></i>Entertainment Center</span>
        <span class="check"><i></i>Laundry Room</span>
        <span class="check"><i></i>Home Office</span>
        <span class="check"><i></i>Garage System</span>
      </div>
    </div>
    <div class="field promo"><label>Enter Promo Code</label><span>SAGE500</span></div>
    <div class="book-btn">Book Now</div>
  </div>
  <p class="appoint-note">We use your zip code to align you with the nearest and best closet designers. We use your email and phone number to contact you and schedule your free design consultation.</p>
</form>

<section class="abs projects">
  <p class="abs projects-eyebrow">Best Case &amp; Studies</p>
  <h2 class="abs projects-title">See Our Latest All Project &amp;<br>Find Best Choose.</h2>
  <div class="abs arrows">
    <span class="arrow arrow-prev"><svg width="10" height="14" viewBox="0 0 10 14"><path d="M8 1 2 7l6 6" fill="none" stroke="#1f1c4d" stroke-width="2"/></svg></span>
    <span class="arrow arrow-next"><svg width="10" height="14" viewBox="0 0 10 14"><path d="M2 1l6 6-6 6" fill="none" stroke="#fff" stroke-width="2"/></svg></span>
  </div>
  <article class="abs card" style="left:28px">
    <div class="card-img" style="background:linear-gradient(180deg,#c9c4bd,#6d6258)" role="img" aria-label="Bedroom closet with hanging clothes"></div>
    <div class="card-body"><h4>Bedroom Closet</h4><p>Closets As Unique As You</p></div>
  </article>
  <article class="abs card" style="left:260px">
    <div class="card-img" style="background:linear-gradient(180deg,#e8e4dd,#9a8a76)" role="img" aria-label="Living room entertainment center"></div>
    <div class="card-body"><h4>Entertainment Center</h4><p>Artfully Entertaining</p></div>
  </article>
  <article class="abs card" style="left:492px">
    <div class="card-img" style="background:linear-gradient(180deg,#f1f0ee,#bdb9b2)" role="img" aria-label="Laundry room with washing machine"></div>
    <div class="card-body"><h4>Laundry Room</h4><p>Make Doing Laundry FUN</p></div>
  </article>
  <article class="abs card" style="left:724px">
    <div class="card-img" style="background:linear-gradient(180deg,#ece6dc,#a88d6c)" role="img" aria-label="Home office with desk and shelving"></div>
    <div class="card-body"><h4>Home Office</h4><p>Make Working From Home Smarter</p></div>
  </article>
  <article class="abs card" style="left:956px">
    <div class="card-img" style="background:linear-gradient(180deg,#8a6a4f,#4e3a2c)" role="img" aria-label="Garage with wall storage system"></div>
    <div class="card-body"><h4>Garage</h4><p>Park In Your Garage And Find Everything</p></div>
  </article>
</section>

<section>
  <div class="abs offer-tall" role="img" aria-label="Model in a light coat, shown from the neck down"></div>
  <div class="abs offer-small" style="left:416px;top:2340px;background:linear-gradient(180deg,#f3f2f0,#e8d678)" role="img" aria-label="Yellow garment on white background"></div>
  <div class="abs offer-small" style="left:416px;top:2506px;background:linear-gradient(180deg,#efeef0,#b9b8bf)" role="img" aria-label="Grey garment on white background"></div>
  <div class="abs offer-line"></div>
  <p class="abs offer-eyebrow">Special Offer</p>
  <h2 class="abs offer-title">Jewelry BOX</h2>
  <p class="abs offer-text">Organize every piece with a custom drawer insert.</p>
  <div class="abs offer-btn">See More Offers
    <svg width="14" height="10" viewBox="0 0 14 10"><path d="M0 5h12M8 1l4 4-4 4" fill="none" stroke="#fff" stroke-width="1.6"/></svg>
  </div>
  <div class="abs steps">
    <div class="step"><span class="step-num">1.</span><div><h5>Easy to use</h5><p>Book a free consultation online.</p></div></div>
    <div class="step"><span class="step-num">2.</span><div><h5>Easy to use</h5><p>We match your local designer.</p></div></div>
    <div class="step"><span class="step-num">3.</span><div><h5>Easy to use</h5><p>Plan your closet with experts.</p></div></div>
    <div class="step"><span class="step-num">4.</span><div><h5>Easy to use</h5><p>Enjoy your new organized space.</p></div></div>
  </div>
</section>

</body>
</html>
```